Business Card Design

I am an child sleep consultant. I would like the picture to be the background of the card and for my logo to be in the upper right hand corner. Other than that, the design is yours!!

Industry/Entity Type

Business

Contact Information for Business Card

Marla Okonov
Tidewell Nestling
Certified Child Sleep Consultant
(406) 555-0193
tidewellnestling.example

```html
<!DOCTYPE html>
<html lang="en">
<head>
<meta charset="utf-8">
<title>Tidewell Nestling — Business Card</title>
<link rel="stylesheet" href="https://fonts.googleapis.com/css2?family=Source+Sans+3:wght@300;400&display=swap">
<style>
  :root {
    --backdrop: #e9e6e2;
    --photo-light: #c9c9c9;
    --photo-mid: #8d8d8d;
    --photo-dark: #3e3e3e;
    --blush: #eadde6;
    --teal: #4fb8c8;
    --teal-deep: #2f8f9e;
    --white: #ffffff;
  }
  * { margin: 0; padding: 0; box-sizing: border-box; }
  html, body {
    width: 1200px;
    height: 1023px;
    overflow: hidden;
    background: var(--backdrop);
    font-family: "Source Sans 3", sans-serif;
  }
  .business-card {
    position: absolute;
    left: 75px;
    top: 211px;
    width: 1050px;
    height: 600px;
    border-radius: 28px;
    overflow: hidden;
    box-shadow: 0 18px 40px rgba(0,0,0,0.18);
    background: var(--photo-mid);
  }
  .card-art {
    position: absolute;
    inset: 0;
    width: 100%;
    height: 100%;
  }
  .brand-mark {
    position: absolute;
    top: 44px;
    right: 52px;
    display: flex;
    align-items: center;
    gap: 14px;
    color: var(--teal-deep);
    font-weight: 400;
    font-size: 30px;
    letter-spacing: 0.5px;
  }
  .brand-dot {
    width: 22px;
    height: 22px;
    border-radius: 50%;
    background: var(--teal-deep);
  }
  .contact-block {
    position: absolute;
    right: 52px;
    top: 320px;
    text-align: right;
    color: var(--white);
    font-weight: 300;
  }
  .contact-name {
    font-size: 44px;
    line-height: 1.1;
    margin-bottom: 14px;
  }
  .contact-line {
    font-size: 25px;
    line-height: 1.5;
  }
</style>
</head>
<body>
  <div class="business-card">
    <svg class="card-art" viewBox="0 0 1050 600" preserveAspectRatio="none">
      <defs>
        <radialGradient id="photoTone" cx="35%" cy="55%" r="75%">
          <stop offset="0" stop-color="var(--photo-light)"/>
          <stop offset="0.55" stop-color="var(--photo-mid)"/>
          <stop offset="1" stop-color="var(--photo-dark)"/>
        </radialGradient>
      </defs>
      <rect class="card-photo" role="img" aria-label="Black-and-white photograph of a baby looking up, filling the card background" x="0" y="0" width="1050" height="600" fill="url(#photoTone)"/>
      <path class="blush-band" d="M620 0 C 575 180, 525 360, 515 600 L1050 600 L1050 0 Z" fill="var(--blush)"/>
      <path class="teal-panel" d="M1050 110 C 820 150, 600 300, 545 600 L1050 600 Z" fill="var(--teal)"/>
    </svg>

    <div class="brand-mark">
      <span class="brand-dot"></span>
      <span class="brand-name">Tidewell Nestling</span>
    </div>

    <div class="contact-block">
      <p class="contact-name">Marla Okonov</p>
      <p class="contact-line">Certified Child Sleep Consultant</p>
      <p class="contact-line">(406) 555-0193</p>
      <p class="contact-line">tidewellnestling.example</p>
    </div>
  </div>
</body>
</html>
```